Format / Design slides - NEED ASAP!!!

Format ONLY slides 4 - 11 and and slide 16.
Make look like slides 12 and 13.

Do NOT worry about slides after the Appendix.
Does not have to look super fancy, just better than what I have.

```html
<!DOCTYPE html>
<html lang="en">
<head>
<meta charset="utf-8">
<title>Harbor REIT – Investor Presentation Slide Overview</title>
<link rel="stylesheet" href="https://fonts.googleapis.com/css2?family=Arimo:wght@400;700&display=swap">
<style>
  :root{
    --stage:#1b2030;
    --paper:#ffffff;
    --navy:#1f3a6e;
    --navy-deep:#16305c;
    --blue:#4a7fc1;
    --sky:#a9c4e0;
    --pale-blue:#dce8f4;
    --green:#6aa84f;
    --lime:#8cc63f;
    --pale-green:#e6f0d6;
    --teal:#3aa6a3;
    --ink:#333a44;
    --muted:#8a919c;
    --label:#c9ced8;
    --select:#e07a5f;
  }
  *{box-sizing:border-box;margin:0;padding:0}
  html,body{width:1200px;height:1000px;overflow:hidden;background:var(--stage);font-family:"Arimo",Arial,sans-serif;color:var(--ink)}
  .sorter{position:absolute;left:12px;top:120px;display:grid;grid-template-columns:repeat(5,224px);column-gap:17px;row-gap:38px}
  .cell{width:224px}
  .slide{position:relative;width:224px;height:158px;background:var(--paper);overflow:hidden}
  .slide.is-active{outline:2px solid var(--select);outline-offset:1px}
  .slide.is-focus{outline:2px solid #d9dde3;outline-offset:1px}
  .num{color:var(--label);font-size:11px;margin-top:6px;padding-left:2px}
  .brand{position:absolute;right:6px;top:4px;display:flex;align-items:center;gap:2px;font-size:4px;font-weight:700;color:var(--navy)}
  .brand i{display:block;width:6px;height:6px;border-radius:50%;background:var(--navy)}
  .foot{position:absolute;left:0;right:0;bottom:0;height:6px;background:var(--navy);font-size:2.6px;color:#fff;padding:1.5px 8px;display:flex;justify-content:space-between}
  .h{position:absolute;left:8px;top:7px;font-size:4.5px;color:var(--navy);letter-spacing:.2px}
  .h.big{font-size:7px;top:7px}
  .sub{position:absolute;left:8px;top:15px;font-size:3.2px;color:var(--green);font-weight:700}
  .tx{font-size:3px;line-height:1.45;color:var(--ink)}
  .abs{position:absolute}
  .bar-navy{background:var(--navy);color:#fff;font-size:3.2px;font-weight:700;padding:1px 3px}
  .box-green{background:var(--pale-green);border:.5px solid var(--green)}
  .box-blue{background:var(--pale-blue);border:.5px solid var(--blue)}
  .hd-green{background:var(--green);color:#fff;font-size:3.4px;font-weight:700;text-align:center;padding:3px 1px}
  .hd-blue{background:var(--sky);color:var(--navy);font-size:3.4px;font-weight:700;text-align:center;padding:3px 1px}
  ul.tx{padding-left:5px}
</style>
</head>
<body>
<main class="sorter">

  <!-- 1 Title -->
  <section class="cell">
    <div class="slide is-active">
      <div class="abs" style="left:10px;top:55px;font-size:10.5px;line-height:1.2;color:var(--navy);letter-spacing:.3px">GROWTH<br>POWERED BY<br>SHOP</div>
      <div class="abs tx" style="left:10px;top:98px;color:var(--muted)">Investor Presentation<br>January 2026</div>
      <div class="abs" style="left:104px;top:60px;display:flex;align-items:center;gap:5px">
        <span style="display:block;width:14px;height:14px;background:var(--blue)"></span>
        <span style="font-size:15px;font-weight:700;color:var(--blue)">Harbor REIT</span>
      </div>
    </div>
    <div class="num">1</div>
  </section>

  <!-- 2 Contents -->
  <section class="cell">
    <div class="slide">
      <div class="brand"><i></i>Harbor REIT</div>
      <div class="abs" style="left:6px;top:14px;width:112px">
        <div class="bar-navy">LEADERSHIP</div>
        <div class="tx" style="padding:2px 3px">Chief Executive · Finance Chief<br>Investment Lead · Asset Lead<br>General Counsel · Accounting Lead<br>Operations Lead · Treasury Lead</div>
        <div class="bar-navy" style="margin-top:3px">BOARD OF DIRECTORS</div>
        <div class="tx" style="padding:2px 3px">Board Chair · Lead Director<br>Audit Chair · Pay Committee<br>Governance Chair · Director</div>
        <div class="bar-navy" style="margin-top:3px">ANALYSTS</div>
        <div class="tx" style="padding:2px 3px">Research desk one · Research desk two<br>Research desk three · Research desk four<br>Research desk five · Research desk six</div>
      </div>
      <div class="abs" style="left:124px;top:14px;width:92px">
        <div class="bar-navy">TABLE OF CONTENTS</div>
        <div class="tx" style="padding:2px 3px">At a Glance ............ 3<br>Highlights ............... 5<br>Compelling Value ...... 6<br>Portfolio Strategy ...... 7<br>Balance Sheet .......... 8<br>Guidance ................. 9<br>SHOP Spotlight ......... 11<br>Transformation ......... 12<br>Fundamentals ........... 15<br>Appendix ................ 16</div>
        <div class="bar-navy" style="margin-top:6px">CONTACT INFORMATION</div>
        <div style="border:.5px solid var(--navy);height:22px;margin-top:2px"></div>
      </div>
      <div class="foot"><span>COMPANY PRESENTATION</span><span>2</span></div>
    </div>
    <div class="num">2</div>
  </section>

  <!-- 3 At a glance -->
  <section class="cell">
    <div class="slide is-focus">
      <div class="brand"><i></i>Harbor REIT</div>
      <div class="h">HARBOR AT-A-GLANCE</div>
      <div class="abs tx" style="left:8px;top:15px;width:208px">Harbor Care Properties, Inc. is a real estate investment trust focused on seniors housing and health care properties, investing through SHOP, triple-net leases, joint ventures and structured finance. Our portfolio includes nearly 200 properties across the U.S.</div>
      <div class="abs" style="left:38px;top:36px;width:150px;height:108px;background:var(--navy);color:#fff;padding:5px 10px">
        <div style="font-size:3px;text-align:center;margin-bottom:4px">AS OF DECEMBER 31, 2025</div>
        <div style="display:grid;grid-template-columns:1fr 1fr;row-gap:5px;font-size:3px">
          <div>Established 1992<br><b style="font-size:6px">NYSE: HBR</b></div>
          <div>Dividend Yield<br><b style="font-size:6px">5.9%</b></div>
          <div>Investment Grade<br><b style="font-size:6px">NAIC 2C rating</b></div>
          <div>Market Value<br><b style="font-size:6px">$1.9B</b></div>
          <div>Total Liquidity<br><b style="font-size:6px">$650.0M</b></div>
          <div>Enterprise Value<br><b style="font-size:6px">$2.8B</b></div>
          <div>Debt to Adj. EBITDAre<br><b style="font-size:6px">4.5x</b></div>
          <div>Debt to Enterprise Value<br><b style="font-size:6px">30.1%</b></div>
        </div>
      </div>
      <div class="foot"><span>COMPANY PRESENTATION</span><span>3</span></div>
    </div>
    <div class="num">3</div>
  </section>

  <!-- 4 Strong growth -->
  <section class="cell">
    <div class="slide">
      <div class="brand"><i></i>Harbor REIT</div>
      <div class="h">HARBOR AT-A-GLANCE</div>
      <div class="abs" style="left:18px;top:68px;font-size:7px;color:var(--navy);line-height:1.3">Strong Growth at a<br>Compelling Value</div>
      <div class="abs" style="left:96px;top:22px;width:118px;display:flex;flex-direction:column;gap:4px">
        <div class="box-green tx" style="padding:2px 3px 2px 12px;position:relative"><span class="abs" style="left:2px;top:3px;width:7px;height:7px;background:var(--lime)"></span><b>Sizeable SHOP growth:</b> portfolio expanded rapidly since 2024 with more to come.</div>
        <div class="box-green tx" style="padding:2px 3px 2px 12px;position:relative"><span class="abs" style="left:2px;top:3px;width:7px;height:7px;background:var(--lime)"></span><b>Internal growth:</b> SHOP NOI rising through operating leverage.</div>
        <div class="box-green tx" style="padding:2px 3px 2px 12px;position:relative"><span class="abs" style="left:2px;top:3px;width:7px;height:7px;background:var(--lime)"></span><b>De-risking:</b> lower exposure to skilled nursing and weaker tenants.</div>
        <div class="box-green tx" style="padding:2px 3px 2px 12px;position:relative"><span class="abs" style="left:2px;top:3px;width:7px;height:7px;background:var(--lime)"></span><b>Solid balance sheet:</b> low leverage and ample liquidity.</div>
        <div class="box-green tx" style="padding:2px 3px 2px 12px;position:relative"><span class="abs" style="left:2px;top:3px;width:7px;height:7px;background:var(--lime)"></span><b>Strategy benefits:</b> multiple expansion potential.</div>
      </div>
      <div class="foot"><span>COMPANY PRESENTATION</span><span>4</span></div>
    </div>
    <div class="num">4</div>
  </section>

  <!-- 5 Highlights -->
  <section class="cell">
    <div class="slide">
      <div class="brand"><i></i>Harbor REIT</div>
      <div class="h">RECENT HIGHLIGHTS (Q3 &amp; Q4)</div>
      <div class="abs" style="left:52px;top:18px;width:56px;height:120px" >
        <div class="hd-blue" style="padding:2px">Q3 2025</div>
        <ul class="tx box-blue" style="height:112px;padding:3px 3px 3px 7px">
          <li>Acquired three SHOP communities for $121M</li>
          <li>Converted six triple-net assets into SHOP</li>
          <li>Sold seven non-core skilled nursing assets</li>
          <li>Raised equity through ATM program</li>
          <li>Extended credit line maturity</li>
        </ul>
      </div>
      <div class="abs" style="left:114px;top:18px;width:56px;height:120px">
        <div class="hd-green" style="padding:2px">Q4 2025</div>
        <ul class="tx box-green" style="height:112px;padding:3px 3px 3px 7px">
          <li>Acquired two SHOP assets for $96M</li>
          <li>Closed loan payoff of $40M</li>
          <li>Added new operator partner</li>
          <li>Over $600M of SHOP assets</li>
        </ul>
      </div>
      <div class="foot"><span>COMPANY PRESENTATION</span><span>5</span></div>
    </div>
    <div class="num">5</div>
  </section>

  <!-- 6 Compelling value -->
  <section class="cell">
    <div class="slide">
      <div class="brand"><i></i>Harbor REIT</div>
      <div class="h big">COMPELLING VALUE</div>
      <div class="sub" style="top:16px;font-size:3.4px">HIGH SHOP CONCENTRATION YET AMONGST LOWEST 2026 AFFO MULTIPLE</div>
      <svg class="abs" style="left:8px;top:24px" width="210" height="122" viewBox="0 0 210 122">
        <line x1="4" y1="4" x2="100" y2="4" stroke="#4a7fc1" stroke-width=".8"/>
        <text x="14" y="10" font-size="3.3" fill="#1f3a6e" font-weight="700">Pro-forma SHOP % of Total NOI</text>
        <line x1="112" y1="4" x2="206" y2="4" stroke="#6aa84f" stroke-width=".8"/>
        <text x="140" y="10" font-size="3.3" fill="#6aa84f" font-weight="700">2026 AFFO Multiple</text>
        <g fill="#a9c4e0">
          <rect x="8" y="26" width="7" height="74"/><rect x="20" y="34" width="7" height="66"/>
          <rect x="32" y="44" width="7" height="56"/><rect x="44" y="58" width="7" height="42"/>
          <rect x="56" y="70" width="7" height="30"/><rect x="68" y="86" width="7" height="14"/>
          <rect x="80" y="96" width="7" height="4"/><rect x="92" y="98" width="7" height="2"/>
        </g>
        <g fill="#6aa84f">
          <rect x="116" y="30" width="7" height="70"/><rect x="128" y="46" width="7" height="54"/>
          <rect x="140" y="52" width="7" height="48"/><rect x="152" y="56" width="7" height="44"/>
          <rect x="164" y="62" width="7" height="38"/><rect x="176" y="66" width="7" height="34"/>
          <rect x="188" y="70" width="7" height="30"/><rect x="200" y="72" width="6" height="28"/>
        </g>
        <g font-size="2.8" fill="#333a44">
          <text x="7" y="24">74%</text><text x="19" y="32">66%</text><text x="31" y="42">56%</text><text x="43" y="56">42%</text>
          <text x="115" y="28">27.1x</text><text x="127" y="44">22.0x</text><text x="139" y="50">19.6x</text><text x="151" y="54">18.0x</text>
        </g>
        <line x1="4" y1="100" x2="102" y2="100" stroke="#8a919c" stroke-width=".4"/>
        <line x1="112" y1="100" x2="208" y2="100" stroke="#8a919c" stroke-width=".4"/>
        <text x="4" y="112" font-size="2.8" fill="#333a44">Source: company filings and consensus estimates</text>
        <text x="112" y="112" font-size="2.8" fill="#6aa84f">Green: SHOP-heavy peer group</text>
      </svg>
      <div class="foot"><span>COMPANY PRESENTATION</span><span>6</span></div>
    </div>
    <div class="num">6</div>
  </section>

  <!-- 7 Portfolio strategy -->
  <section class="cell">
    <div class="slide">
      <div class="brand"><i></i>Harbor REIT</div>
      <div class="h">FOCUSED PORTFOLIO STRATEGY TO ENHANCE SHAREHOLDER RETURNS</div>
      <div class="abs" style="left:20px;top:42px;width:58px">
        <div class="hd-green">Increasing Internal Growth Through SHOP</div>
        <ul class="tx box-green" style="height:74px;padding:3px 3px 3px 7px"><li>Acquire existing seniors housing communities</li><li>Replace lower-growth triple-net rent with SHOP NOI</li></ul>
      </div>
      <div class="abs" style="left:83px;top:42px;width:58px">
        <div class="hd-green">Accelerating External Growth</div>
        <ul class="tx box-green" style="height:74px;padding:3px 3px 3px 7px"><li>Opportunistic acquisitions with strong operators</li><li>Acquired $600M+ of SHOP since 2024</li><li>Higher yield on invested capital</li></ul>
      </div>
      <div class="abs" style="left:146px;top:42px;width:58px">
        <div class="hd-blue">Reducing Portfolio Risk</div>
        <ul class="tx box-blue" style="height:74px;padding:3px 3px 3px 7px"><li>Lower nursing exposure</li><li>Increasing tenant and operator diversity</li><li>Reducing average asset age and improving quality</li></ul>
      </div>
      <div class="foot"><span>COMPANY PRESENTATION</span><span>7</span></div>
    </div>
    <div class="num">7</div>
  </section>

  <!-- 8 Balance sheet -->
  <section class="cell">
    <div class="slide">
      <div class="brand"><i></i>Harbor REIT</div>
      <div class="h">SOLID BALANCE SHEET</div>
      <svg class="abs" style="left:18px;top:55px" width="186" height="46" viewBox="0 0 186 46">
        <polygon points="0,6 170,6 186,23 170,40 0,40" fill="#dce8f4"/>
      </svg>
      <div class="abs" style="left:20px;top:58px;width:54px;height:28px;background:var(--teal);color:#fff;font-size:6px;font-weight:700;text-align:center;padding-top:3px;line-height:1.3">Liquidity:<br>$542.0 million*</div>
      <ul class="abs tx" style="left:84px;top:63px;width:100px;padding-left:5px"><li>$26 million cash on hand</li><li>$516 million available on unsecured line</li><li>$200 million available under ATM</li></ul>
      <div class="abs tx" style="left:22px;top:92px">*Pro forma</div>
      <div class="foot"><span>COMPANY PRESENTATION</span><span>8</span></div>
    </div>
    <div class="num">8</div>
  </section>

  <!-- 9 Guidance -->
  <section class="cell">
    <div class="slide">
      <div class="brand"><i></i>Harbor REIT</div>
      <div class="h">GUIDANCE</div>
      <div class="abs" style="left:8px;top:18px;width:208px;height:72px;background:var(--pale-green);padding:3px 5px">
        <div class="tx" style="font-weight:700;color:var(--green)">Assumptions</div>
        <ul class="tx" style="padding-left:6px">
          <li>Guidance excludes investments not yet announced and any future capital raising.</li>
          <li>Interest expense range of $44 million to $46 million for the full year.</li>
          <li>SHOP NOI expected in the range of $60 million to $64 million.</li>
          <li>Triple-net rent and interest income of $90 million to $93 million.</li>
          <li>General and administrative expenses of $28 million to $30 million.</li>
        </ul>
      </div>
      <div class="abs" style="left:8px;top:96px;width:208px;font-size:3px">
        <div style="display:grid;grid-template-columns:2fr 1fr 1fr;border-bottom:.5px solid var(--navy);padding:1px 0;font-weight:700"><span></span><span>Full Year</span><span>First Quarter</span></div>
        <div style="display:grid;grid-template-columns:2fr 1fr 1fr;background:var(--pale-blue);padding:1.5px 0"><span>Diluted earnings per share</span><span>$1.60 to $1.64</span><span>$0.40 to $0.41</span></div>
        <div style="display:grid;grid-template-columns:2fr 1fr 1fr;padding:1.5px 0"><span>Diluted FFO per share</span><span>$2.70 to $2.75</span><span>$0.68 to $0.69</span></div>
        <div style="display:grid;grid-template-columns:2fr 1fr 1fr;background:var(--pale-blue);padding:1.5px 0"><span>Diluted Core FFO per share</span><span>$2.80 to $2.84</span><span>$0.70 to $0.71</span></div>
      </div>
      <div class="foot"><span>COMPANY PRESENTATION</span><span>9</span></div>
    </div>
    <div class="num">9</div>
  </section>

  <!-- 10 Quotes -->
  <section class="cell">
    <div class="slide">
      <div class="brand"><i></i>Harbor REIT</div>
      <div class="abs" style="left:36px;top:20px;width:112px;height:36px;background:var(--pale-green);padding:3px 4px">
        <div class="tx">"Our strategy to scale SHOP is reshaping the growth profile of the company, and we remain disciplined in selecting partners and assets that add long-term value."</div>
        <div class="tx" style="text-align:right;font-weight:700">— Chief Executive</div>
      </div>
      <div class="abs" style="left:110px;top:62px;width:114px;height:52px;background:var(--teal);padding:4px 5px;color:#fff">
        <div class="tx" style="color:#fff">"The transformation of our portfolio toward private-pay seniors housing has improved visibility into earnings and gives us a clear runway for growth in 2026."</div>
        <div class="tx" style="color:#fff;text-align:right;font-weight:700;margin-top:2px">— Finance Chief</div>
      </div>
      <div class="foot"><span>COMPANY PRESENTATION</span><span>10</span></div>
    </div>
    <div class="num">10</div>
  </section>

  <!-- 11 SHOP spotlight -->
  <section class="cell">
    <div class="slide">
      <div class="brand"><i></i>Harbor REIT</div>
      <div class="h">SHOP SPOTLIGHT</div>
      <svg class="abs" style="left:56px;top:14px" width="112" height="118" viewBox="0 0 112 118">
        <g font-size="3.2" fill="#fff" text-anchor="middle" font-weight="700">
          <polygon points="56,0 74,10 74,30 56,40 38,30 38,10" fill="#3aa6a3"/><text x="56" y="19">10 YEARS</text><text x="56" y="24" font-weight="400">average age</text>
          <polygon points="22,20 40,30 40,50 22,60 4,50 4,30" fill="#6aa84f"/><text x="22" y="38">76% NOI</text><text x="22" y="43" font-weight="400">growth</text>
          <polygon points="90,20 108,30 108,50 90,60 72,50 72,30" fill="#8cc63f"/><text x="90" y="39">7</text><text x="90" y="44" font-weight="400">operators</text>
          <polygon points="56,40 74,50 74,70 56,80 38,70 38,50" fill="#a9d08e"/><text x="56" y="59">$455</text><text x="56" y="64" font-weight="400">million</text>
          <polygon points="22,60 40,70 40,90 22,100 4,90 4,70" fill="#6aa84f"/><text x="22" y="79">34%</text><text x="22" y="84" font-weight="400">of NOI</text>
          <polygon points="90,60 108,70 108,90 90,100 72,90 72,70" fill="#3aa6a3"/><text x="90" y="79">27%</text><text x="90" y="84" font-weight="400">margin</text>
          <polygon points="56,78 74,88 74,108 56,118 38,108 38,88" fill="#3aa6a3"/><text x="56" y="98">3,000+</text><text x="56" y="103" font-weight="400">units</text>
        </g>
      </svg>
      <div class="abs tx" style="left:10px;top:136px;width:204px">With SHOP now comprising 37% of our total assets, we believe the platform is positioned to drive above-average, higher-quality growth.</div>
      <div class="foot"><span>COMPANY PRESENTATION</span><span>11</span></div>
    </div>
    <div class="num">11</div>
  </section>

  <!-- 12 Transformation -->
  <section class="cell">
    <div class="slide">
      <div class="brand"><i></i>Harbor REIT</div>
      <div class="h">SENIORS HOUSING OPERATING PORTFOLIO ("SHOP") TRANSFORMATION</div>
      <div class="abs" style="left:8px;top:18px;width:100px">
        <div class="tx" style="color:var(--green);font-weight:700;border-bottom:.5px solid var(--green)">2025 SHOP ACTIVITIES SINCE 1/1/25</div>
        <ul class="tx" style="padding:2px 0 0 6px"><li>$484M+ SHOP acquisitions</li><li>$69M+ three SHOP conversions</li><li>Seven SHOP operators, five new</li></ul>
        <div class="tx" style="color:var(--green);font-weight:700;border-bottom:.5px solid var(--green);margin-top:6px">2025 SHOP CONVERSIONS</div>
        <ul class="tx" style="padding:2px 0 0 6px"><li>$59M completed in 1Q26</li><li>$30M expected over next 60 days</li><li>Two SHOP operators, both new</li></ul>
        <div class="tx" style="color:var(--green);font-weight:700;border-bottom:.5px solid var(--green);margin-top:6px">2026 SHOP INVESTMENT GUIDANCE</div>
        <ul class="tx" style="padding:2px 0 0 6px"><li>$80M SHOP acquisitions completed</li><li>$271M SHOP acquisitions next 60 days</li><li>$125M+ SHOP acquisitions expected</li></ul>
      </div>
      <div class="abs" style="left:118px;top:18px;width:98px">
        <div class="tx" style="color:var(--green);font-weight:700;border-bottom:.5px solid var(--green)">SHOP GROWTH</div>
        <svg width="98" height="66" viewBox="0 0 98 66">
          <rect x="14" y="48" width="14" height="10" fill="#a9c4e0"/><rect x="40" y="34" width="14" height="24" fill="#6aa84f"/><rect x="66" y="14" width="14" height="44" fill="#6aa84f"/>
          <path d="M10 48 L86 6" stroke="#6aa84f" stroke-width="1.4" fill="none"/><path d="M82 5 L87 5 L85 10" stroke="#6aa84f" stroke-width="1.2" fill="none"/>
          <line x1="8" y1="58" x2="92" y2="58" stroke="#8a919c" stroke-width=".4"/>
          <g font-size="3" fill="#333a44" text-anchor="middle"><text x="21" y="63">2024</text><text x="47" y="63">2025</text><text x="73" y="63">Q1 2026 PF</text><text x="73" y="12">$455</text></g>
        </svg>
        <div class="tx" style="color:var(--green);font-weight:700;border-bottom:.5px solid var(--green);margin-top:2px">2026 INVESTMENT FUNDING</div>
        <ul class="tx" style="padding:2px 0 0 6px"><li>$358M liquidity from ATM and loan payoffs</li><li>Proceeds from dispositions of assets</li></ul>
      </div>
      <div class="foot"><span>COMPANY PRESENTATION</span><span>12</span></div>
    </div>
    <div class="num">12</div>
  </section>

  <!-- 13 Portfolio transformation charts -->
  <section class="cell">
    <div class="slide">
      <div class="brand"><i></i>Harbor REIT</div>
      <div class="h">PORTFOLIO TRANSFORMATION: DECREASING SNF AND LOAN EXPOSURE</div>
      <svg class="abs" style="left:6px;top:14px" width="212" height="136" viewBox="0 0 212 136">
        <g font-size="3" fill="#6aa84f" font-weight="700">
          <text x="2" y="5">ASSET TYPE TRANSFORMATION</text><text x="108" y="5">INVESTMENT TYPE TRANSFORMATION</text>
          <text x="2" y="22">GROSS INVESTMENT BY ASSET TYPE</text><text x="108" y="22">GROSS INVESTMENT BY INVESTMENT TYPE</text>
          <text x="2" y="86">NOI BY ASSET TYPE</text><text x="108" y="86">NOI BY INVESTMENT TYPE</text>
        </g>
        <g font-size="2.7" fill="#333a44">
          <text x="2" y="10">SHOP share rising as nursing exposure declines</text><text x="108" y="10">Triple-net and loans shrink as SHOP scales up</text>
        </g>
        <g>
          <rect x="12" y="30" width="14" height="48" fill="#6aa84f"/><rect x="12" y="30" width="14" height="20" fill="#8cc63f"/><rect x="12" y="60" width="14" height="18" fill="#4a7fc1"/>
          <rect x="40" y="28" width="14" height="50" fill="#6aa84f"/><rect x="40" y="28" width="14" height="16" fill="#a9d08e"/><rect x="40" y="62" width="14" height="16" fill="#4a7fc1"/>
          <rect x="68" y="26" width="14" height="52" fill="#8cc63f"/><rect x="68" y="50" width="14" height="14" fill="#6aa84f"/><rect x="68" y="64" width="14" height="14" fill="#4a7fc1"/>
          <rect x="118" y="30" width="14" height="48" fill="#3aa6a3"/><rect x="118" y="30" width="14" height="14" fill="#8cc63f"/>
          <rect x="146" y="28" width="14" height="50" fill="#3aa6a3"/><rect x="146" y="28" width="14" height="20" fill="#8cc63f"/>
          <rect x="174" y="26" width="14" height="52" fill="#3aa6a3"/><rect x="174" y="26" width="14" height="30" fill="#8cc63f"/>
        </g>
        <g>
          <ellipse cx="76" cy="108" rx="20" ry="12" fill="#6aa84f"/><path d="M76 108 L76 96 A20 12 0 0 1 96 108 Z" fill="#8cc63f"/><path d="M76 108 L96 108 A20 12 0 0 1 80 120 Z" fill="#a9d08e"/>
          <ellipse cx="182" cy="108" rx="20" ry="12" fill="#6aa84f"/><path d="M182 108 L182 96 A20 12 0 0 1 202 108 Z" fill="#8cc63f"/>
        </g>
        <g font-size="2.6" fill="#333a44">
          <rect x="4" y="96" width="3" height="3" fill="#8cc63f"/><text x="9" y="99">Assisted living</text>
          <rect x="4" y="102" width="3" height="3" fill="#6aa84f"/><text x="9" y="105">Memory care</text>
          <rect x="4" y="108" width="3" height="3" fill="#4a7fc1"/><text x="9" y="111">Skilled nursing</text>
          <rect x="110" y="96" width="3" height="3" fill="#8cc63f"/><text x="115" y="99">SHOP</text>
          <rect x="110" y="102" width="3" height="3" fill="#6aa84f"/><text x="115" y="105">Triple-net</text>
          <rect x="110" y="108" width="3" height="3" fill="#3aa6a3"/><text x="115" y="111">Loans</text>
        </g>
      </svg>
      <div class="foot"><span>COMPANY PRESENTATION</span><span>13</span></div>
    </div>
    <div class="num">13</div>
  </section>

  <!-- 14 Portfolio recycling -->
  <section class="cell">
    <div class="slide">
      <div class="brand"><i></i>Harbor REIT</div>
      <div class="abs" style="left:26px;top:16px;width:176px;height:22px;background:#e8ecf1;text-align:center;font-size:5.2px;color:var(--blue);padding-top:3px;line-height:1.3">Portfolio Recycling + SHOP Acquisitions =<br><b>Powerful Driver of Earnings &amp; Value Creation</b></div>
      <svg class="abs" style="left:8px;top:42px" width="210" height="104" viewBox="0 0 210 104">
        <rect x="6" y="6" width="8" height="34" fill="#16305c"/><rect x="20" y="20" width="8" height="20" fill="#3aa6a3"/><rect x="34" y="26" width="8" height="14" fill="#8cc63f"/><rect x="48" y="12" width="8" height="28" fill="#4a7fc1"/><rect x="62" y="30" width="8" height="10" fill="#a9c4e0"/>
        <line x1="2" y1="40" x2="76" y2="40" stroke="#8a919c" stroke-width=".4"/>
        <text x="4" y="58" font-size="3.2" fill="#333a44">WACC · 70% Debt / 30% Equity</text>
        <rect x="10" y="64" width="8" height="22" fill="#6aa84f"/><rect x="26" y="70" width="8" height="16" fill="#3aa6a3"/><rect x="42" y="74" width="8" height="12" fill="#4a7fc1"/>
        <line x1="6" y1="86" x2="56" y2="86" stroke="#8a919c" stroke-width=".4"/>
        <g fill="#3aa6a3"><polygon points="84,14 100,14 100,10 108,18 100,26 100,22 84,22"/><polygon points="84,78 100,78 100,74 108,82 100,90 100,86 84,86"/></g>
        <text x="114" y="20" font-size="3.6" fill="#16305c">SHOP 300 BP Spread To Sale Yield</text>
        <text x="122" y="36" font-size="3" fill="#333a44">Expected After Year-5 IRR SHOP</text>
        <rect x="120" y="42" width="8" height="16" fill="#4a7fc1"/><rect x="134" y="46" width="8" height="12" fill="#6aa84f"/><rect x="148" y="40" width="8" height="18" fill="#3aa6a3"/><rect x="162" y="44" width="8" height="14" fill="#a9c4e0"/>
        <text x="114" y="84" font-size="3.6" fill="#16305c">SHOP 700 BP Spread To WACC</text>
      </svg>
      <div class="foot"><span>COMPANY PRESENTATION</span><span>14</span></div>
    </div>
    <div class="num">14</div>
  </section>

  <!-- 15 Industry fundamentals -->
  <section class="cell">
    <div class="slide">
      <div class="brand"><i></i>Harbor REIT</div>
      <div class="h">FAVORABLE INDUSTRY FUNDAMENTALS</div>
      <svg class="abs" style="left:6px;top:16px" width="110" height="62" viewBox="0 0 110 62">
        <text x="55" y="4" font-size="2.8" fill="#333a44" text-anchor="middle">U.S. Senior Population Growth by Age Bracket</text>
        <path d="M8 48 L30 44 L52 38 L74 30 L100 24" stroke="#a9c4e0" stroke-width="1" fill="none"/>
        <path d="M8 40 L30 36 L52 30 L74 26 L100 20" stroke="#8cc63f" stroke-width="1" fill="none"/>
        <path d="M8 30 L30 22 L52 16 L74 14 L100 12" stroke="#6aa84f" stroke-width="1" fill="none"/>
        <line x1="6" y1="54" x2="104" y2="54" stroke="#8a919c" stroke-width=".4"/>
      </svg>
      <ol class="abs tx" style="left:122px;top:20px;width:96px;padding-left:6px;color:var(--navy)">
        <li>Demographics and limited new supply drive occupancy higher and above-average rate growth.</li>
        <li style="margin-top:3px">Construction starts are at historical lows.</li>
        <li style="margin-top:3px">Years 2026 through 2030 represent acquisition opportunities at below-replacement cost.</li>
      </ol>
      <svg class="abs" style="left:6px;top:84px" width="212" height="62" viewBox="0 0 212 62">
        <text x="50" y="4" font-size="2.8" fill="#333a44" text-anchor="middle">Inventory vs. Demand Growth</text>
        <g fill="#4a7fc1"><rect x="10" y="20" width="6" height="30"/><rect x="20" y="16" width="6" height="34"/><rect x="30" y="22" width="6" height="28"/><rect x="40" y="26" width="6" height="24"/><rect x="50" y="28" width="6" height="22"/><rect x="60" y="30" width="6" height="20"/><rect x="70" y="34" width="6" height="16"/><rect x="80" y="36" width="6" height="14"/></g>
        <path d="M10 24 L86 12" stroke="#e07a5f" stroke-width=".8" fill="none"/>
        <line x1="6" y1="50" x2="96" y2="50" stroke="#8a919c" stroke-width=".4"/>
        <text x="158" y="4" font-size="2.8" fill="#333a44" text-anchor="middle">Seniors Housing Units Under Construction</text>
        <g><rect x="114" y="14" width="6" height="36" fill="#3aa6a3"/><rect x="124" y="12" width="6" height="38" fill="#3aa6a3"/><rect x="134" y="16" width="6" height="34" fill="#3aa6a3"/><rect x="144" y="22" width="6" height="28" fill="#3aa6a3"/><rect x="154" y="28" width="6" height="22" fill="#e07a5f"/><rect x="164" y="34" width="6" height="16" fill="#e07a5f"/><rect x="174" y="38" width="6" height="12" fill="#e07a5f"/><rect x="184" y="40" width="6" height="10" fill="#e07a5f"/><rect x="194" y="42" width="6" height="8" fill="#e07a5f"/></g>
        <line x1="110" y1="50" x2="206" y2="50" stroke="#8a919c" stroke-width=".4"/>
        <text x="4" y="58" font-size="2.6" fill="#333a44">Source: industry market data, company estimates</text>
      </svg>
      <div class="foot"><span>COMPANY PRESENTATION</span><span>15</span></div>
    </div>
    <div class="num">15</div>
  </section>

  <!-- 16 Case study -->
  <section class="cell">
    <div class="slide">
      <div class="brand"><i></i>Harbor REIT</div>
      <div class="h">HYPOTHETICAL CASE STUDY</div>
      <div class="abs tx" style="left:8px;top:15px;width:208px">The following hypothetical example illustrates how converting a triple-net lease to SHOP may lift NOI over time as occupancy and margins recover.</div>
      <div class="abs" style="left:28px;top:36px;width:160px;font-size:2.8px;color:var(--ink)">
        <div style="font-weight:700;margin-bottom:2px">Hypothetical Conversion Illustration (in $ thousands)</div>
        <div style="display:grid;grid-template-columns:2fr 1fr 1fr 1fr 1fr;background:var(--pale-blue);padding:1px 0;font-weight:700"><span>Occupancy Change</span><span>Yr 1</span><span>Yr 2</span><span>Yr 3</span><span>Yr 4</span></div>
        <div style="display:grid;grid-template-columns:2fr 1fr 1fr 1fr 1fr;padding:1px 0"><span>Units</span><span>120</span><span>120</span><span>120</span><span>120</span></div>
        <div style="display:grid;grid-template-columns:2fr 1fr 1fr 1fr 1fr;padding:1px 0"><span>Occupancy</span><span>80.0%</span><span>84.0%</span><span>88.0%</span><span>91.0%</span></div>
        <div style="display:grid;grid-template-columns:2fr 1fr 1fr 1fr 1fr;padding:1px 0"><span>Occupied units</span><span>96</span><span>101</span><span>106</span><span>109</span></div>
        <div style="display:grid;grid-template-columns:2fr 1fr 1fr 1fr 1fr;padding:1px 0"><span>Revenue</span><span>6,900</span><span>7,450</span><span>8,020</span><span>8,510</span></div>
        <div style="display:grid;grid-template-columns:2fr 1fr 1fr 1fr 1fr;padding:1px 0"><span>Expenses</span><span>5,300</span><span>5,480</span><span>5,690</span><span>5,860</span></div>
        <div style="display:grid;grid-template-columns:2fr 1fr 1fr 1fr 1fr;padding:1px 0"><span>NOI</span><span>1,600</span><span>1,970</span><span>2,330</span><span>2,650</span></div>
        <div style="display:grid;grid-template-columns:2fr 1fr 1fr 1fr 1fr;padding:1px 0"><span>Margin</span><span>23.2%</span><span>26.4%</span><span>29.1%</span><span>31.1%</span></div>
        <div style="height:4px"></div>
        <div style="display:grid;grid-template-columns:2fr 1fr 1fr 1fr 1fr;padding:1px 0;border-top:.5px solid var(--navy)"><span>Revenue</span><span>7,150</span><span>7,300</span><span>7,480</span><span>7,620</span></div>
        <div style="display:grid;grid-template-columns:2fr 1fr 1fr 1fr 1fr;padding:1px 0"><span>Expenses</span><span>5,400</span><span>5,460</span><span>5,520</span><span>5,590</span></div>
        <div style="display:grid;grid-template-columns:2fr 1fr 1fr 1fr 1fr;padding:1px 0"><span>NOI</span><span>1,750</span><span>1,840</span><span>1,960</span><span>2,030</span></div>
        <div style="display:grid;grid-template-columns:2fr 1fr 1fr 1fr 1fr;background:var(--pale-blue);padding:1px 0;font-weight:700"><span>Spread</span><span>(150)</span><span>130</span><span>370</span><span>620</span></div>
        <div style="height:4px"></div>
        <div style="display:grid;grid-template-columns:2fr 1fr 1fr 1fr 1fr;padding:1px 0"><span>Revenue Growth</span><span></span><span>8.0%</span><span>7.7%</span><span>6.1%</span></div>
        <div style="display:grid;grid-template-columns:2fr 1fr 1fr 1fr 1fr;padding:1px 0"><span>Expense Growth</span><span></span><span>3.4%</span><span>3.8%</span><span>3.0%</span></div>
        <div style="display:grid;grid-template-columns:2fr 1fr 1fr 1fr 1fr;padding:1px 0"><span>NOI Change</span><span></span><span>23.1%</span><span>18.3%</span><span>13.7%</span></div>
      </div>
      <div class="foot"><span>COMPANY PRESENTATION</span><span>16</span></div>
    </div>
    <div class="num">16</div>
  </section>

</main>
</body>
</html>
```